Sample Book Covers University Press

We need three (simple) sample book FRONT covers designed, which will represent the look and feel of a new university press. This institution is a leader in Depth Psychology, Mythology and Humanities.

The covers should use the same template, font etc.
Each cover will have a different color font and a different image.

Please see attached document for text.
Font: Close to Pacifica Font attached, this should also be one of the colors.
Other font colors green and blue, which can be different from the ones in the document.

Back round color should be close to the sample, or the the attached file.

These will be sample files, we will not use them on actual books, so feel free to use other images representing the categories. (or the ones in the image)

Questions? Please feel free to contact us.

University

```html
<!DOCTYPE html>
<html lang="en">
<head>
<meta charset="utf-8">
<title>University Press – Sample Covers</title>
<link rel="stylesheet" href="https://fonts.googleapis.com/css2?family=Marcellus&family=Open+Sans:wght@700&display=swap">
<style>
  :root {
    --page-bg: #ffffff;
    --frame-white: #ffffff;
    --band-text: #ffffff;

    --hum-light: #fffde8;
    --hum-edge: #f6e868;
    --hum-title: #4aae48;
    --hum-band-top: #a3c64a;
    --hum-band-bottom: #6f9d2c;
    --hum-art-a: #e4e4e4;
    --hum-art-b: #b9bcc4;
    --hum-art-c: #9a8fb8;

    --myth-light: #e9f6fd;
    --myth-edge: #44b3e8;
    --myth-title: #1d4c9b;
    --myth-band-top: #3c8ad0;
    --myth-band-bottom: #1a5aa6;

    --depth-light: #fff8dc;
    --depth-edge: #fcbd2a;
    --depth-title: #d97a1e;
    --depth-band-top: #f9a13a;
    --depth-band-bottom: #f28a12;
  }
  * { margin: 0; padding: 0; box-sizing: border-box; }
  html, body {
    width: 1200px; height: 638px; overflow: hidden;
    background: var(--page-bg);
  }
  .covers {
    position: relative; width: 1200px; height: 638px;
  }
  .cover {
    position: absolute; top: 46px; width: 363px; height: 540px;
    overflow: hidden;
  }
  .cover--humanities { left: 34px;
    background: radial-gradient(ellipse 75% 70% at 50% 50%, var(--hum-light) 0%, var(--hum-edge) 100%); }
  .cover--mythology { left: 420px;
    background: radial-gradient(ellipse 75% 70% at 50% 50%, var(--myth-light) 0%, var(--myth-edge) 100%); }
  .cover--depth { left: 805px;
    background: radial-gradient(ellipse 75% 70% at 50% 50%, var(--depth-light) 0%, var(--depth-edge) 100%); }

  .cover__art {
    position: absolute; left: 76px; top: 59px;
    width: 200px; height: 210px;
    border: 5px solid var(--frame-white);
  }
  .cover--humanities .cover__art {
    background: linear-gradient(135deg, var(--hum-art-a) 0%, var(--hum-art-b) 55%, var(--hum-art-c) 100%);
  }
  .cover--mythology .cover__art {
    background: linear-gradient(135deg, #d8b49a 0%, #c99a7a 45%, #b8783c 70%, #a3231e 100%);
  }
  .cover--depth .cover__art {
    background: linear-gradient(180deg, #f4f6f6 0%, #eaeaea 100%);
  }

  .cover__title {
    position: absolute; left: 0; right: 0;
    font-family: "Marcellus", serif;
    font-weight: 400; font-size: 45px; letter-spacing: 1px;
    text-align: center; line-height: 50px; white-space: nowrap;
  }
  .cover--humanities .cover__title { top: 322px; color: var(--hum-title); }
  .cover--mythology .cover__title { top: 322px; color: var(--myth-title); }
  .cover--depth .cover__title { top: 295px; color: var(--depth-title); }

  .cover__band {
    position: absolute; left: 0; right: 0; bottom: 0; height: 61px;
    display: flex; align-items: center; justify-content: center;
    font-family: "Open Sans", sans-serif; font-weight: 700;
    font-size: 27px; color: var(--band-text);
  }
  .cover--humanities .cover__band { background: linear-gradient(var(--hum-band-top), var(--hum-band-bottom)); }
  .cover--mythology .cover__band { background: linear-gradient(var(--myth-band-top), var(--myth-band-bottom)); }
  .cover--depth .cover__band { background: linear-gradient(var(--depth-band-top), var(--depth-band-bottom)); }
</style>
</head>
<body>
<main class="covers">
  <section class="cover cover--humanities">
    <div class="cover__art" role="img" aria-label="Photo of a human eye with a multicoloured iris"></div>
    <h2 class="cover__title">HUMANITIES</h2>
    <div class="cover__band">Coastline Press</div>
  </section>

  <section class="cover cover--mythology">
    <div class="cover__art" role="img" aria-label="Photo of a golden carved dragon against a red pillar"></div>
    <h2 class="cover__title">MYTHOLOGY</h2>
    <div class="cover__band">Coastline Press</div>
  </section>

  <section class="cover cover--depth">
    <div class="cover__art" role="img" aria-label="Illustration of a tree whose crown is made of colourful hand prints"></div>
    <h2 class="cover__title">DEPTH<br>PSYCHOLOGY</h2>
    <div class="cover__band">Coastline Press</div>
  </section>
</main>
</body>
</html>
```